I need someone to design an advertisement using the attached information, will be used for industrial product. I want logo on the top, the arrows pointing towards the corresponding feature on product photo and the bottom to have the square boxes filled with info and graphics provided. This is just an outline of what I would like feel free do get creative. Thanks!

Target Market(s)

consumer

Industry/Entity Type

Graphic Design

Colors
ec1f27

```html
<!DOCTYPE html>
<html lang="en">
<head>
<meta charset="utf-8">
<title>Post Driver Feature Sheet</title>
<link rel="stylesheet" href="https://fonts.googleapis.com/css2?family=Poppins:wght@500;600;700&family=Archivo+Black&display=swap">
<style>
  :root {
    --ink: #111111;
    --bg-center: #ffffff;
    --bg-edge: #d9d9d9;
    --steel-light: #e6e7e8;
    --steel-mid: #a9acb0;
    --steel-dark: #2a2a2c;
    --paper: #ffffff;
    --rule: #555555;
    --accent: #ec1f27;
  }
  html, body {
    margin: 0;
    padding: 0;
    width: 1108px;
    height: 1200px;
    overflow: hidden;
  }
  body {
    background: radial-gradient(ellipse at 50% 40%, var(--bg-center) 0%, #f1f1f1 45%, var(--bg-edge) 100%);
    font-family: "Poppins", Arial, sans-serif;
    color: var(--ink);
  }
  .stage {
    position: relative;
    width: 1000px;
    height: 1083px;
    transform: scale(1.108);
    transform-origin: 0 0;
  }
  .product-photo {
    position: absolute;
    left: 345px;
    top: 170px;
    width: 320px;
    height: 550px;
    border-radius: 18px;
    background: linear-gradient(90deg, var(--steel-mid) 0%, var(--steel-light) 35%, #c8cacd 60%, var(--steel-dark) 100%);
  }
  .callouts {
    position: absolute;
    inset: 0;
    width: 1000px;
    height: 1083px;
  }
  .label {
    position: absolute;
    font-weight: 600;
    font-size: 17px;
    line-height: 19px;
    letter-spacing: 0.6px;
    margin: 0;
    white-space: nowrap;
  }
  .label--right { text-align: right; }
  .label-warranty { right: 787px; top: 200px; }
  .label-piston { right: 759px; top: 350px; }
  .label-housing { left: 110px; top: 462px; }
  .label-barrel { left: 80px; top: 596px; }
  .label-throttle { left: 838px; top: 287px; }
  .label-damping { left: 685px; top: 455px; }
  .label-inner-barrel { left: 763px; top: 610px; }

  .benefits {
    position: absolute;
    left: 197px;
    top: 838px;
    display: flex;
    gap: 35px;
  }
  .benefit {
    width: 92px;
    display: flex;
    flex-direction: column;
    align-items: center;
  }
  .benefit-badge {
    width: 72px;
    height: 72px;
    margin-bottom: 10px;
  }
  .benefit-card {
    width: 92px;
    height: 92px;
    background: var(--ink);
    border-radius: 8px;
    color: var(--paper);
    text-align: center;
    box-sizing: border-box;
    padding-top: 10px;
  }
  .benefit-title {
    font-family: "Archivo Black", Arial, sans-serif;
    font-size: 13px;
    line-height: 12px;
    margin: 0 0 6px;
    letter-spacing: 0.2px;
  }
  .benefit-rule {
    width: 74px;
    height: 1px;
    background: var(--rule);
    margin: 0 auto 7px;
  }
  .benefit-text {
    font-size: 7.5px;
    line-height: 9.5px;
    font-weight: 500;
    margin: 0 8px;
  }
</style>
</head>
<body>
<main class="stage">
  <div class="product-photo" role="img" aria-label="Petrol powered post driver with silver cast housing, red and black engine, twin handles and black removable barrel"></div>

  <svg class="callouts" viewBox="0 0 1000 1083" aria-hidden="true" fill="none" stroke="#111" stroke-width="1.6">
    <polyline points="118,248 230,248 236,270 241,228 245,248 425,248"/>
    <line x1="248" y1="358" x2="460" y2="358"/>
    <line x1="286" y1="334" x2="286" y2="381"/>
    <circle cx="286" cy="358" r="7" fill="#111"/>
    <circle cx="286" cy="334" r="3.5" fill="#111"/>
    <circle cx="286" cy="381" r="3.5" fill="#111"/>
    <line x1="249" y1="344" x2="268" y2="331" stroke-width="1.3"/>
    <circle cx="249" cy="344" r="2.5" fill="#111"/>
    <circle cx="268" cy="331" r="2.5" fill="#111"/>
    <line x1="215" y1="451" x2="475" y2="451"/>
    <path d="M255 633 Q295 633 295 600 L295 565 Q295 533 328 533 L432 533"/>
    <circle cx="295" cy="582" r="10" fill="#fff" stroke-width="2"/>
    <polygon points="295,577 299.3,579.5 299.3,584.5 295,587 290.7,584.5 290.7,579.5" fill="#111" stroke="none"/>
    <path d="M530 350 L735 350 Q770 350 772 318 L774 292 Q777 268 805 268 L832 268"/>
    <line x1="832" y1="274" x2="940" y2="274" stroke-width="1.4"/>
    <g stroke-width="1.4">
      <line x1="834" y1="262" x2="834" y2="274"/>
      <line x1="843" y1="268" x2="843" y2="274"/>
      <line x1="852" y1="268" x2="852" y2="274"/>
      <line x1="861" y1="268" x2="861" y2="274"/>
      <line x1="870" y1="264" x2="870" y2="274"/>
      <line x1="879" y1="268" x2="879" y2="274"/>
      <line x1="888" y1="268" x2="888" y2="274"/>
      <line x1="897" y1="268" x2="897" y2="274"/>
      <line x1="906" y1="264" x2="906" y2="274"/>
      <line x1="915" y1="268" x2="915" y2="274"/>
      <line x1="924" y1="268" x2="924" y2="274"/>
      <line x1="933" y1="268" x2="933" y2="274"/>
      <line x1="940" y1="262" x2="940" y2="274"/>
    </g>
    <line x1="540" y1="437" x2="683" y2="437"/>
    <g fill="#111" stroke="none">
      <circle cx="690" cy="437" r="1"/>
      <circle cx="698" cy="437" r="1.3"/>
      <circle cx="706" cy="437" r="1.6"/>
      <circle cx="716" cy="437" r="2"/>
      <circle cx="728" cy="437" r="2.5"/>
    </g>
    <line x1="490" y1="598" x2="798" y2="598"/>
    <circle cx="728" cy="598" r="11" fill="#111" stroke="none"/>
    <path d="M722 598 H734 M728 592 V604" stroke="#fff" stroke-width="2.4"/>
    <circle cx="757" cy="578" r="9" fill="#111" stroke="none"/>
    <path d="M752 578 H762 M757 573 V583" stroke="#fff" stroke-width="2"/>
  </svg>

  <p class="label label--right label-warranty">Lifetime impact<br>waranty</p>
  <p class="label label--right label-piston">Industry Leading<br>Polymer Piston</p>
  <p class="label label-housing">Cast Hoysing</p>
  <p class="label label-barrel">Removable Barrel</p>
  <p class="label label-throttle">Precision<br>Throttle</p>
  <p class="label label-damping">Damping System<br>Reduces Fatigue</p>
  <p class="label label-inner-barrel">Anodized 3 1/8 in<br>Inner Barrel</p>

  <section class="benefits">
    <article class="benefit">
      <svg class="benefit-badge" viewBox="0 0 72 72" role="img" aria-label="Hand assembled family owned seal">
        <circle cx="36" cy="36" r="33" fill="none" stroke="#111" stroke-width="1.6"/>
        <circle cx="36" cy="36" r="26" fill="#111"/>
      </svg>
      <div class="benefit-card">
        <h3 class="benefit-title">QUALITY</h3>
        <div class="benefit-rule"></div>
        <p class="benefit-text">Family<br>owned company<br>takes pride<br>in work</p>
      </div>
    </article>

    <article class="benefit">
      <svg class="benefit-badge" viewBox="0 0 72 72" role="img" aria-label="Open hand with sparkles icon">
        <circle cx="36" cy="36" r="33" fill="none" stroke="#111" stroke-width="1.6"/>
        <circle cx="36" cy="38" r="17" fill="#111"/>
      </svg>
      <div class="benefit-card">
        <h3 class="benefit-title">VALUE</h3>
        <div class="benefit-rule"></div>
        <p class="benefit-text">Save thousands<br>on labour/fuel</p>
      </div>
    </article>

    <article class="benefit">
      <svg class="benefit-badge" viewBox="0 0 72 72" role="img" aria-label="Three year satisfaction guarantee seal">
        <circle cx="36" cy="36" r="33" fill="none" stroke="#111" stroke-width="1.6"/>
        <circle cx="36" cy="36" r="26" fill="#111"/>
      </svg>
      <div class="benefit-card">
        <h3 class="benefit-title">PEACE<br>OF MIND</h3>
        <p class="benefit-text">Industry Leading<br>3 years of warranty</p>
      </div>
    </article>

    <article class="benefit">
      <svg class="benefit-badge" viewBox="0 0 72 72" role="img" aria-label="National flag emblem">
        <circle cx="36" cy="36" r="33" fill="none" stroke="#111" stroke-width="1.6"/>
        <circle cx="36" cy="36" r="27" fill="#2b2b2b"/>
      </svg>
      <div class="benefit-card">
        <h3 class="benefit-title">PRIDE</h3>
        <div class="benefit-rule"></div>
        <p class="benefit-text">Australian made<br>components<br>assembled in USA</p>
      </div>
    </article>

    <article class="benefit">
      <svg class="benefit-badge" viewBox="0 0 72 72" role="img" aria-label="Support agent with headset icon">
        <circle cx="36" cy="36" r="33" fill="none" stroke="#111" stroke-width="1.6"/>
        <circle cx="36" cy="36" r="20" fill="#111"/>
      </svg>
      <div class="benefit-card">
        <h3 class="benefit-title">SERVICE<br>SUPPORT</h3>
        <p class="benefit-text">Dedicated USA<br>service facility<br>and phone<br>support</p>
      </div>
    </article>
  </section>
</main>
</body>
</html>
```